パック詰めしたカニ身を入れる袋のデザインを依頼させていただきます。中の商品が見えるように、また通販のお客様だけでなく、デパートの食品売り場や高級スーパーで手にとっていただけるような、高級感のあるデザイン案をお願いします。イメージは『和モダン』です。
▼デザインの仕様▼
【袋サイズ】W200×H300(mm)
【デザインしていただく部分】W200×H270(mm)
※袋下30mmは空けておいてください。
商品が入った状態の参考画像は添付ファイル①を参照
(今回は袋のデザインをお願いします)
【色の数】4色まで
【材質】PP

▼記載内容▼※文字サイズ、字体、配置はおまかせいたします。
【商品名】右記よりどれか(かに身 ・ カニ身 ・ 蟹身)
【会社名】北岡商店
【賞味期限印刷用スペース】W30×H10(mm)※白抜きで
【商品特長】以下よりいくつか選択の上記載してください。
※表現は自由に変更してください。
・茹でへのこだわり(アルカリ水、瀬波の白粒使用)
・兵庫 香住港産
・日本海の深層水で育まれた
・みずみずしい
・カニ本来の甘み
【イメージ画像】添付ファイル②参照
※こちらは使っていただいてもいただかなくてもどちらでも結構です。
赤系、グレー系、黒・ゴールド等、高級感のある色
• 高解像度JPG (.jpg)
• イラストレーター形式 (.ai)
参考画像追記しておきます
多くのご提案ありがとうございます。
ご検討いただいているランサーの皆様に弊社よりお願いがあります。

1.依頼開始当初より記載しておりました、『和モダン』というイメージにあまり固執されすぎることなく、各ランサー様の自由な発想でデザインしていただきたい。
2.添付ファイル②のカニの画像は使用しないでください。

大変申し訳ございませんが、既にご提案いただいております皆様も、上記の点を踏まえまして、再度のご検討、ご提案いただければと思います。
残り日数少ない中、急な変更ではございますが何卒宜しくお願い致します。
上記変更に伴い、締め切りを1日延長させていただきます。
よろしくお願いいたします

ご質問等ございましたら、お気軽にお問い合わせ下さい。

・伝えたいことを見ただけで分かりやすくとらえることができる。
・主張しすぎないデザインの中に、高級感、上品さが感じ取れる。
・バランスがよく、中のカニ身を引き立ててくれると感じた。

皆様の貴重なお時間を、弊社依頼に費やしていただきまして、誠にありがとうございました。
今回見送らせていただいた皆様のご提案の中にも、素晴らしいデザインのものが数多くありました。今後もTesmora内におきまして他製品のパッケージやパンフレット等の依頼ができればと思っております。その際は是非また、素敵なご提案をお願いいたします。

```html
<!DOCTYPE html>
<html lang="ja">
<head>
<meta charset="UTF-8">
<title>かに身 パッケージ</title>
<link href="https://fonts.googleapis.com/css2?family=Shippori+Mincho:wght@500;700;800&family=Yuji+Syuku&display=swap" rel="stylesheet">
<style>
  :root {
    --paper: #ffffff;
    --ink: #0b0b0b;
    --gold-light: #f3df8a;
    --gold: #d4ab3c;
    --gold-deep: #8f6a16;
    --brand-red: #c7341f;
    --text-white: #f6f2ea;
    --meat-cream: #f4e3d0;
    --meat-pink: #e79a86;
    --crab-red: #d4461f;
    --crab-orange: #ef8a3e;
  }
  * { margin: 0; padding: 0; box-sizing: border-box; }
  html, body {
    width: 840px;
    height: 1200px;
    overflow: hidden;
    background: var(--paper);
  }
  .package {
    position: relative;
    width: 840px;
    height: 1200px;
    background: var(--paper);
    font-family: "Shippori Mincho", serif;
  }
  .gold-band {
    position: absolute;
    left: 62px;
    top: 72px;
    width: 716px;
    height: 104px;
    background: linear-gradient(180deg, var(--gold-light) 0%, var(--gold) 45%, var(--gold-deep) 100%);
  }
  .black-panel {
    position: absolute;
    left: 62px;
    top: 176px;
    width: 716px;
    height: 871px;
    background: var(--ink);
    overflow: hidden;
  }
  .brand {
    position: absolute;
    left: 32px;
    top: 22px;
    display: flex;
    align-items: center;
    gap: 10px;
  }
  .brand-dot {
    width: 30px;
    height: 30px;
    border-radius: 50%;
    background: var(--brand-red);
  }
  .brand-name {
    font-size: 24px;
    font-weight: 700;
    color: var(--brand-red);
    letter-spacing: 2px;
  }
  .origin {
    position: absolute;
    left: 0;
    right: 0;
    top: 44px;
    text-align: center;
    font-size: 30px;
    font-weight: 700;
    color: var(--text-white);
    letter-spacing: 4px;
  }
  .product-name {
    position: absolute;
    left: 0;
    right: 0;
    top: 78px;
    text-align: center;
    font-family: "Yuji Syuku", serif;
    font-size: 138px;
    line-height: 1.15;
    letter-spacing: 18px;
    background: linear-gradient(180deg, var(--gold-light) 10%, var(--gold) 55%, var(--gold-deep) 100%);
    -webkit-background-clip: text;
    background-clip: text;
    color: transparent;
  }
  .window {
    position: absolute;
    left: 134px;
    top: 244px;
    width: 462px;
    height: 252px;
    clip-path: polygon(12% 0, 88% 0, 100% 50%, 88% 100%, 12% 100%, 0 50%);
    background: linear-gradient(90deg, var(--meat-pink) 0%, var(--meat-cream) 30%, var(--meat-pink) 55%, var(--meat-cream) 80%, var(--meat-pink) 100%);
  }
  .crab-photo {
    position: absolute;
    left: 0;
    top: 454px;
    width: 560px;
    height: 417px;
    background: radial-gradient(ellipse at 55% 55%, var(--crab-orange) 0%, var(--crab-red) 35%, #5a1608 65%, var(--ink) 88%);
  }
  .feature-copy {
    position: absolute;
    left: 580px;
    top: 470px;
    writing-mode: vertical-rl;
    white-space: nowrap;
    font-size: 20px;
    font-weight: 500;
    line-height: 2.1;
    letter-spacing: 1px;
    color: var(--text-white);
  }
  .feature-copy span { display: block; }
</style>
</head>
<body>
  <div class="package">
    <div class="gold-band"></div>
    <section class="black-panel">
      <div class="brand">
        <span class="brand-dot"></span>
        <span class="brand-name">北岡商店</span>
      </div>
      <p class="origin">兵庫 香住港産</p>
      <h1 class="product-name">かに身</h1>
      <div class="window" role="img" aria-label="パック詰めされた棒状のカニ身の写真"></div>
      <div class="crab-photo" role="img" aria-label="皿に盛られた茹でガニの写真"></div>
      <p class="feature-copy"><span>日本海の深層水で育まれた</span><span>みずみずしいカニ本来の甘み</span><span>をご堪能ください</span></p>
    </section>
  </div>
</body>
</html>
```